Redesign of existing website for a corporate advisory business focussed on technology

We need a redesign of our website. We are a corporate advisory business based in Sydney. Our focus is on the technology and life-science sectors. We assist our clients with capital raisings, mergers and acquisitions and other corporate transactions.

Our business is called "Harbourline Capital Advisors"
Our current website is www.harbourlinecap.com.au

I'd like to see a complete re-design of the site. (I'm happy to keep any of the existing images - but equally happy to scrap them completely and "start again".)

My preference is that the logo remain as it is. However, I would be very open to a re-colouring of the logo if it works better with a new webiste design.

The content of the website will remain the same. I'd like one additional section - "News" - which will allow us to manually post news items and which will pull in news feeds from current and past clients.

In terms of positioning / look-and-feel:

Our clients fall into two categories. I'd like the website to appeal to both:

1. The first category is: Executives from established technology or life-science companies (private or public), who engage us to assist with strategy, capital raising, corporate transactions.

2. The second category is: Entrepreneurs looking for advice in accessing angel funding or venture capital. The site should appeal to young tech-savvy entrepreneurs who are looking to engage a firm to provide such assistance.

To accomodate both target groups, the overriding feel should be one of professionalism, stability, trust and expertise. However, while the site should look fairly "corporate", I'd like it to feel contemporary and have an element of creativity and flair, reflecting the fact that our clients are often early-stage, innovative, technology companies. (I know this might be a tricky balance...)

Target Market(s)

Potential clients. Typically executives at technology or life-science companies or (more typically) entrepreneurs building their own companies

Industry/Entity Type

Business

Requirements
Must have
• 1. All content on the existing website
2. An additional section called "News" that allows us to easily add news items or articles and ideally which accepts news feeds from a handful of past and present clients
3. An ability to easily update and edit content
Should not have
• The site should not have "gimmicks". (Definitely no devices like the moving arrow in the current site!)

It should be fairly conservative, while still feeling contemporary and fresh.

```html
<!DOCTYPE html>
<html lang="en">
<head>
<meta charset="utf-8">
<title>Our team — Harbourline Capital Advisors</title>
<link rel="stylesheet" href="https://fonts.googleapis.com/css2?family=Arimo:wght@400;700&display=swap">
<style>
  :root {
    --orange: #f58a45;
    --ink: #1f1f1f;
    --text: #333333;
    --muted: #777777;
    --header-bg: #ececec;
    --photo-bg: #e4e4e4;
    --photo-tone: #cfcfcf;
    --rule: #b5b5b5;
    --page: #ffffff;
  }
  * { box-sizing: border-box; margin: 0; padding: 0; }
  html, body { width: 1200px; height: 988px; overflow: hidden; background: var(--page); }
  body { position: relative; font-family: "Arimo", Arial, sans-serif; color: var(--text); }

  .site-header { position: absolute; left: 0; top: 0; width: 1200px; height: 175px; }
  .header-texture { position: absolute; inset: 0; background: var(--header-bg); border-bottom: 1px solid #e2e2e2; }
  .brand { position: absolute; left: 122px; top: 46px; }
  .brand-name { font-size: 27px; font-weight: 400; color: #444; letter-spacing: 0.5px; line-height: 34px; }

  .main-nav a { position: absolute; top: 144px; font-size: 18px; color: var(--ink); text-decoration: none; }
  .main-nav a.is-current { color: #8a8a8a; }

  .breadcrumb { position: absolute; left: 122px; top: 200px; font-size: 12px; font-weight: 700; display: flex; align-items: center; gap: 10px; }
  .breadcrumb .crumb-home { color: var(--ink); }
  .breadcrumb .crumb-current { color: var(--muted); }

  .page-title { position: absolute; left: 122px; top: 246px; font-size: 18px; font-weight: 700; color: var(--orange); }
  .page-intro { position: absolute; left: 123px; top: 284px; font-size: 12.5px; color: var(--text); }

  .team-member { position: absolute; top: 352px; width: 320px; }
  .member-name { font-size: 15px; font-weight: 700; color: #444; letter-spacing: 0.2px; }
  .member-photo { width: 92px; height: 92px; border-radius: 50%; margin: 17px 0 0 10px;
    background: linear-gradient(180deg, var(--photo-bg) 0%, var(--photo-tone) 100%); }
  .member-details { margin: 25px 0 0 1px; font-size: 12px; line-height: 18px; color: var(--text); }
  .read-more { font-weight: 700; color: #333; text-decoration: none; }

  .site-footer { position: absolute; left: 121px; top: 685px; width: 958px; border-top: 1px solid var(--rule); text-align: center; }
  .site-footer p { margin-top: 26px; font-size: 12px; color: var(--text); }
</style>
</head>
<body>
  <header class="site-header">
    <div class="header-texture" role="img" aria-label="Faint light grey geometric pattern background"></div>
    <div class="brand">
      <span class="brand-name">Harbourline Capital Advisors</span>
    </div>
    <nav class="main-nav">
      <a href="#" style="left:122px">Home</a>
      <a href="#" style="left:268px">News</a>
      <a href="#" style="left:416px">Our services</a>
      <a href="#" class="is-current" style="left:611px">Our team</a>
      <a href="#" style="left:784px">Our experience</a>
      <a href="#" style="left:997px">Contact us</a>
    </nav>
  </header>

  <nav class="breadcrumb">
    <span class="crumb-home">Home</span>
    <svg width="7" height="10" viewBox="0 0 7 10"><path d="M1 1l4 4-4 4" fill="none" stroke="#888" stroke-width="1.2"/></svg>
    <span class="crumb-current">Our team</span>
  </nav>

  <h1 class="page-title">A dedicated senior team with a wealth of experience</h1>
  <p class="page-intro">Harbourline Capital Advisors brings together a senior team of corporate advisory and investment professionals, committed to the long-term success of our clients.</p>

  <section class="team-member" style="left:123px">
    <h2 class="member-name">Daniel Whitcombe</h2>
    <div class="member-photo" role="img" aria-label="Black and white portrait photo of Daniel Whitcombe"></div>
    <p class="member-details">Executive Director<br>daniel.whitcombe@harbourlinecap.com.au<br>+61 2 9410 3382<br><a class="read-more" href="#">Read more</a></p>
  </section>

  <section class="team-member" style="left:434px">
    <h2 class="member-name">Marcus Feldstein</h2>
    <div class="member-photo" role="img" aria-label="Black and white portrait photo of Marcus Feldstein"></div>
    <p class="member-details">Executive Director<br>marcus.feldstein@harbourlinecap.com.au<br>+61 2 9410 3381<br><a class="read-more" href="#">Read more</a></p>
  </section>

  <section class="team-member" style="left:765px">
    <h2 class="member-name">Oliver Brennan</h2>
    <div class="member-photo" role="img" aria-label="Black and white portrait photo of Oliver Brennan"></div>
    <p class="member-details">Director<br>oliver.brennan@harbourlinecap.com.au<br>+61 2 9517 2206<br><a class="read-more" href="#">Read more</a></p>
  </section>

  <footer class="site-footer">
    <p>Harbourline Capital Advisors Pty Ltd 2011, AFS License No: 517260</p>
  </footer>
</body>
</html>
```